Business Card Design

This is a new business to be run from my home. I have attended certificate workshops run by Dr Kevin Ruddock who is a Master Trainer in Gentle Flow for Mobility.
I wish to communicate to people that Tai Chi is for everyone, no matter their age, gender or fitness levels. Tai Chi is taught both standing & seated.
The card should have a slightly Asian feel, mainly printed in black & white with perhaps a little soft pink &/or green.

Target Market(s)

people of all ages from 10 years up, poor fitness & mild disabilities.

Industry/Entity Type

Fitness

Contact Information for Business Card

Marrowdene Flowing Arts for Body, Mind & Stillness

Brenna Holcroft, Certificated Leader

ph 5281 9046

Requirements
Nice to have
• a feeling of health & peace.
Should not have
• bright colours, fancy fonts

```html
<!DOCTYPE html>
<html lang="en">
<head>
<meta charset="utf-8">
<title>Marrowdene Flowing Arts – Business Card</title>
<link rel="stylesheet" href="https://fonts.googleapis.com/css2?family=Poppins:wght@500;600&family=Poiret+One&display=swap">
<style>
  :root {
    --ink: #111111;
    --paper: #ffffff;
    --wash-light: #eef9e4;
    --wash-mid: #cdeeb4;
    --wash-deep: #a9dd88;
    --vine-dark: #2b3a26;
  }
  * { margin: 0; padding: 0; box-sizing: border-box; }
  html, body {
    width: 1200px;
    height: 741px;
    overflow: hidden;
    background: var(--paper);
  }
  .card {
    position: relative;
    width: 1200px;
    height: 741px;
    overflow: hidden;
    color: var(--ink);
    background:
      radial-gradient(ellipse 420px 300px at 330px 370px, var(--paper) 0%, rgba(255,255,255,0) 100%),
      linear-gradient(120deg, var(--wash-mid) 0%, var(--wash-light) 35%, var(--paper) 55%, var(--wash-light) 80%, var(--wash-mid) 100%);
  }
  .card__floral {
    position: absolute;
    top: 0;
    right: 0;
    width: 600px;
    height: 741px;
    clip-path: polygon(100px 0, 600px 0, 600px 741px, 180px 741px, 0 420px, 40px 250px);
    background:
      radial-gradient(circle at 70% 30%, rgba(43,58,38,0.55) 0%, rgba(43,58,38,0) 45%),
      radial-gradient(circle at 75% 75%, rgba(43,58,38,0.5) 0%, rgba(43,58,38,0) 45%),
      linear-gradient(160deg, var(--wash-deep) 0%, var(--wash-light) 50%, var(--wash-mid) 100%);
    opacity: 0.85;
  }
  .card__text { position: absolute; left: 81px; z-index: 1; white-space: nowrap; }
  .business-name {
    top: 86px;
    font-family: "Poppins", sans-serif;
    font-weight: 600;
    font-size: 48px;
    letter-spacing: 0.5px;
  }
  .business-tagline {
    top: 152px;
    font-family: "Poiret One", sans-serif;
    font-size: 40px;
  }
  .leader-name {
    top: 318px;
    font-family: "Poppins", sans-serif;
    font-weight: 600;
    font-size: 56px;
  }
  .leader-title {
    top: 392px;
    left: 168px;
    font-family: "Poiret One", sans-serif;
    font-size: 46px;
  }
  .phone {
    top: 606px;
    font-family: "Poppins", sans-serif;
    font-weight: 500;
    font-size: 38px;
  }
</style>
</head>
<body>
  <div class="card">
    <div class="card__floral" role="img" aria-label="Black swirling vine ornament with small flowers over soft green leaf wash"></div>
    <h1 class="card__text business-name">Marrowdene Flowing Arts</h1>
    <p class="card__text business-tagline">for Body, Mind &amp; Stillness</p>
    <p class="card__text leader-name">Brenna Holcroft</p>
    <p class="card__text leader-title">Certified Leader</p>
    <p class="card__text phone">ph 5281 9046</p>
  </div>
</body>
</html>
```